Corvane Holdings need Brochure/Portfolio. We need someone who can insert info graphic and graphic back ground etc. Upon request, company logo and other pictures can be sent to the designer. See attachments. The attachment titled"Marketing letter" includes the word content for the Brochure Design, and the attachment titled "Brochure Ideas" includes the word content for our Website Design.

Target Market(s)

Dispensary, Growers and Producer

Industry/Entity Type

Laboratory

Number of Pages Required

5+ page

Font styles to use
Decorative

Colors
add136

Requirements
Must have
• follow RQLT guideline
• 4.1 Overall design of any submission should be tasteful, respectful, and medically-focused. The look must be “medical” or “pharmaceutical,” and should contain no reference to or perception of being high, fun or recreational in nature. Names, logos, signs or advertisements most likely to be approved will not
• appeal to minors, contain cartoon*-like figures or illustrations or contain attempts at humor.
• 4.2 Preferred typography selections include using clean fonts (sans serif), and avoiding script, decorative or gimmicky fonts. It is preferred that a maximum of two fonts and three colors are used in the designs.
• 4.3 Acceptable words or references include, but are not limited to: green; wellness; compassion; health; patient; therapy; care; garden; nature; marijuana; and cannabis.
• 4.4 Designers shall avoid making unfounded claims or promises or using the word “cure.”
• 4.5 Designers shall avoid using marijuana slang such as bud, pot, weed, grass, joint, doobie, 420.
• 4.6 All logos submitted for approval must also be used on business cards, letterhead, and any other types of stationery used by the MME, as well as any advertisements purchased by the MME. Different logos, other than those approved by the Administrator, will not be permitted.
Nice to have
• Info graphic
Should not have
• Cartoon: Cartoon, defined: a sketch or drawing, usually humorous, as in a newspaper or periodical, symbolizing, satirizing, or caricaturing some action, subject or person of popular interest. (wordvault.example)

```html
<!DOCTYPE html>
<html lang="en">
<head>
<meta charset="utf-8">
<title>Corvane Laboratory – Brochure Spread</title>
<link rel="stylesheet" href="https://fonts.googleapis.com/css2?family=Lato:wght@400;700;900&family=Oswald:wght@500;600&family=Michroma&family=Days+One&display=swap">
<style>
  :root {
    --backdrop: #6a4a2c;
    --page: #ffffff;
    --page-shade: #eeeeee;
    --green-dark: #2f4a12;
    --green: #4f7219;
    --green-olive: #5d7f1e;
    --green-light: #add136;
    --ink: #1e1e1e;
    --grey: #555555;
  }
  * { margin: 0; padding: 0; box-sizing: border-box; }
  html, body { width: 1200px; height: 907px; overflow: hidden; }
  body { background: var(--backdrop); position: relative; font-family: "Lato", sans-serif; }

  .spread { position: absolute; left: 65px; top: 65px; width: 1075px; height: 770px; }
  .page { position: absolute; top: 0; height: 770px; overflow: hidden; }
  .page--left { left: 0; width: 535px; background: linear-gradient(90deg, var(--page) 0%, var(--page) 85%, var(--page-shade) 100%); }
  .page--right { left: 535px; width: 540px; background: linear-gradient(90deg, var(--page-shade) 0%, var(--page) 8%); }

  .forest-fill { position: absolute; left: 0; top: 420px; width: 535px; height: 290px;
    background: linear-gradient(180deg, rgba(255,255,255,1) 0%, rgba(196,205,185,.55) 45%, rgba(170,182,160,.6) 100%); }

  .section { position: absolute; left: 35px; width: 463px; }
  .section--intro { top: 38px; }
  .section--potency { top: 246px; }
  .section__title { display: flex; align-items: center; gap: 5px; font-family: "Michroma", sans-serif; font-size: 13.5px; line-height: 20px; color: var(--green); letter-spacing: .2px; margin-bottom: 5px; }
  .section__bullet { width: 17px; height: 19px; flex: none; }
  .section__body { font-weight: 700; font-size: 12.4px; line-height: 15.2px; color: var(--ink); text-align: justify; }

  .tile { position: absolute; overflow: visible; }
  .tile--dark { left: -12px; top: 460px; width: 100px; height: 156px; }
  .tile--mid { left: 18px; top: 580px; width: 144px; height: 162px; }
  .tile--call { left: 155px; top: 580px; width: 144px; height: 162px; }
  .call { position: absolute; left: 155px; top: 580px; width: 144px; height: 162px;
    display: flex; flex-direction: column; align-items: center; justify-content: center; gap: 2px; }
  .call__label { font-family: "Days One", sans-serif; font-size: 18px; line-height: 24px; color: var(--ink); letter-spacing: 1px; }
  .call__number { font-family: "Oswald", sans-serif; font-weight: 600; font-size: 26px; line-height: 30px; color: var(--ink); display: inline-block; transform: scaleX(.82); }

  .band--green { position: absolute; left: 0; top: 713px; width: 535px; height: 28px; background: var(--green); }

  .brand { position: absolute; left: 120px; top: 28px; display: flex; align-items: center; gap: 14px; }
  .brand__name { font-family: "Lato", sans-serif; font-weight: 700; font-size: 30px; line-height: 29px; color: var(--grey); text-align: right; }
  .brand__square { width: 44px; height: 44px; background: var(--green-dark); }

  .rule { position: absolute; left: 0; width: 540px; background: var(--green); }
  .rule--top { top: 153px; height: 7px; }
  .rule--bottom { top: 534px; height: 8px; }

  .photo-main { position: absolute; left: 0; top: 167px; width: 537px; height: 365px;
    background: linear-gradient(120deg, #6f8f4a 0%, #b9c7a6 35%, #d8dcd2 50%, #5f823a 75%, #3e5e22 100%); }

  .hex-photo { position: absolute; }
  .hex-photo--leaf { left: 280px; top: 385px; width: 145px; height: 160px; }
  .hex-photo--trees { left: 345px; top: 510px; width: 160px; height: 180px; }

  .headline { position: absolute; left: 15px; top: 580px; width: 310px; }
  .headline__main { font-family: "Oswald", sans-serif; font-weight: 600; font-size: 40px; line-height: 46px; color: var(--green-dark); white-space: nowrap; transform: scaleX(.79); transform-origin: left center; }
  .headline__sub { font-family: "Lato", sans-serif; font-weight: 900; font-size: 23.5px; line-height: 28px; color: var(--green-olive); white-space: nowrap; }
  .headline__tail { font-family: "Days One", sans-serif; font-size: 28px; line-height: 40px; color: var(--ink); letter-spacing: .3px; white-space: nowrap; }

  .band--black { position: absolute; left: 0; top: 713px; width: 540px; height: 28px;
    background: linear-gradient(90deg, #000 0%, #1a1a1a 70%, #555 100%); }
</style>
</head>
<body>
<main class="spread">
  <section class="page page--left">
    <div class="forest-fill" role="img" aria-label="Faint photograph of a misty forest"></div>

    <article class="section section--intro">
      <h2 class="section__title"><svg class="section__bullet" viewBox="0 0 17 19"><polygon points="8.5,0 17,4.75 17,14.25 8.5,19 0,14.25 0,4.75" fill="var(--green-dark)"/></svg>INTRODUCTION</h2>
      <p class="section__body">Cannabis growers and producers benefit tremendously from cannabis testing! We test your product in order to meet state requirements, for product certifica&shy;tion, and to reduce the risk of contamination. We use scientifically validated meth&shy;ods that ensures that the consumers are receiving accurately labeled products that are free from contamination. Corvane Laboratory delivers total medical mari&shy;juana quality testing solutions for: potency, terpenes, pesticides, residual solvents, heavy metals, moisture content, microbes and foreign matter, and mycotoxins. We provide packages which test in compliance with NAC453A for required state tests, or packages based on your testing needs. We will test any sample upon your re&shy;quest. And guess what? The first two samples that we receive are tested for free. Completely on us!</p>
    </article>

    <article class="section section--potency">
      <h2 class="section__title"><svg class="section__bullet" viewBox="0 0 17 19"><polygon points="8.5,0 17,4.75 17,14.25 8.5,19 0,14.25 0,4.75" fill="var(--green-dark)"/></svg>POTENCY ANALYSIS</h2>
      <p class="section__body">The most important component in cannabis testing is determining accurate canna&shy;binoidconcentrations in the sample. THC and cannabinoid content is responsible for producing the psychoactive effects of the plant and is measured in a variety of medicinal cannabis products including edibles, waxes, dry products, and infusions. Many medical conditions require differing amounts of cannabinoids present in the product in order to tailor to the patients’ medical needs. So it is important, as with all pharmaceuticals, that the appropriate dosage be given to the patient.<br>Potency analysis ensures that your product be tested for its concentration of can&shy;nabinoids with optimal accuracy. In order to provide a full profile of the cannabi&shy;noids being analyzed, we utilize ultra-high performance liquid chromatography (UHPLC). The UHPLC delivers maximum reliability and stability, automating can&shy;nabis potency tests with exceptional ease.</p>
    </article>

    <div class="band--green"></div>
    <svg class="tile tile--dark" viewBox="0 0 100 156"><polygon points="50,3 97,30 97,126 50,153 -40,126 -40,30" fill="var(--green-dark)" stroke="#fff" stroke-width="4"/></svg>
    <svg class="tile tile--mid" viewBox="0 0 144 162"><polygon points="72,3 141,42 141,120 72,159 3,120 3,42" fill="var(--green)" stroke="#fff" stroke-width="4"/></svg>
    <svg class="tile tile--call" viewBox="0 0 144 162"><polygon points="72,3 141,42 141,120 72,159 3,120 3,42" fill="var(--green-light)" stroke="#fff" stroke-width="4"/></svg>
    <div class="call">
      <span class="call__label">CALL</span>
      <span class="call__number">0123456789</span>
    </div>
  </section>

  <section class="page page--right">
    <div class="brand">
      <span class="brand__name">Corvane<br>Laboratory</span>
      <span class="brand__square"></span>
    </div>

    <div class="rule rule--top"></div>
    <div class="photo-main" role="img" aria-label="Photograph of a scientist in a lab coat inspecting cannabis plants in a green field"></div>
    <div class="rule rule--bottom"></div>

    <svg class="hex-photo hex-photo--leaf" viewBox="0 0 145 160" role="img" aria-label="Close-up photograph of a cannabis leaf">
      <defs>
        <linearGradient id="leafTone" x1="0" y1="0" x2="1" y2="1">
          <stop offset="0" stop-color="#a9c25a"/><stop offset="1" stop-color="#6d8a30"/>
        </linearGradient>
      </defs>
      <polygon points="72.5,3 141,42 141,118 72.5,157 4,118 4,42" fill="url(#leafTone)" stroke="#ffffff" stroke-width="5"/>
    </svg>

    <svg class="hex-photo hex-photo--trees" viewBox="0 0 160 180" role="img" aria-label="Photograph of sunlit green forest canopy">
      <defs>
        <linearGradient id="treeTone" x1="0" y1="0" x2="0" y2="1">
          <stop offset="0" stop-color="#c9e27a"/><stop offset="1" stop-color="#4c7a1c"/>
        </linearGradient>
      </defs>
      <polygon points="80,4 156,47 156,133 80,176 4,133 4,47" fill="#ffffff" stroke="var(--green-light)" stroke-width="6"/>
      <polygon points="80,16 145,53 145,127 80,164 15,127 15,53" fill="url(#treeTone)"/>
    </svg>

    <div class="headline">
      <p class="headline__main">WE TEST YOUR PRODUCT</p>
      <p class="headline__sub">IN ORDER TO MEET STATE</p>
      <p class="headline__tail">REQUIREMENTS</p>
    </div>

    <div class="band--black"></div>
  </section>
</main>
</body>
</html>
```